**Kestrel Joinery Works Limited**

We need a website for a renovation/remodeling company based in Hamilton, New Zealand. Ideally it will catch clients' attention and be modern and professional looking. I have attached a logo that I have just recently had made (through PixelForge). If the website could reflect this style and colour schemes, that would be awesome. The final design should communicate a trustworthiness and professionalism.

I have attached photos of a website that I really think is great, so if we could have something that follows along those likes,

https://www.dailyquillpost.example/local-news/news/hamilton-builder-named-top-apprentice-in-region/QXPLTZ8VRA3MJ5FDYHUNCESKWB/

I won a competition a few years ago while I was an apprentice, If we could somehow put that in there as one of my achievements to try to bring in some trust that would be awesome. I would like to add a new picture though because my beard in that photo is wild.

Target Market(s)

Families that want live in the homes that i'm working on. not investors. People that are looking for quality not cheapest price.

Industry/Entity Type

Construction, Home renovations, Maintenance, Deck Builds, New Builds, Bathrooms, Kitchens

Coding

Number of Pages Required

5+ page

Font styles to use
Sans Serif

Colors
6B429C
8869AF
B7A5CE
E3DAEB
F3F0F8

Requirements
Must have
• Contact us page, large clear pictures, Colours the work with the purple in my logo. That will be my company colour so I'm thinking black and purple, or what ever compliments purple nicely
Nice to have
• Page for Renovations, Testimonials, Contact us, Home, About us
Should not have
• Plain looking pages, empty white space, I want the text to be beside a nice big picture etc

```html
<!DOCTYPE html>
<html lang="en">
<head>
<meta charset="utf-8">
<title>Kestrel Joinery Works Limited</title>
<link href="https://fonts.googleapis.com/css2?family=Montserrat:wght@700;800;900&family=Poppins:wght@400;500;600;700&display=swap" rel="stylesheet">
<style>
:root{
  --purple:#6B429C;
  --purple-mid:#8869AF;
  --purple-soft:#B7A5CE;
  --purple-pale:#E3DAEB;
  --purple-mist:#F3F0F8;
  --ink:#161616;
  --ink-deep:#0f0f0f;
  --slate:#3d3d3f;
  --white:#ffffff;
  --grey-text:#555;
  --gold:#f4b400;
}
*{box-sizing:border-box;margin:0;padding:0}
html,body{width:1200px;height:4818px;overflow:hidden}
body{position:relative;background:var(--white);font-family:'Poppins',sans-serif;color:var(--ink)}
.block{position:absolute;overflow:hidden}
.photo{position:absolute;inset:0}
.deco{position:absolute;inset:0;width:100%;height:100%}
.display{font-family:'Montserrat',sans-serif;font-weight:900;text-transform:uppercase;color:var(--white);letter-spacing:1px}
.outline{color:transparent;-webkit-text-stroke:2px var(--white)}
.copy{position:absolute;color:var(--white);font-size:12.5px;line-height:24px}
.btn{position:absolute;display:flex;align-items:center;justify-content:center;font-size:10px;font-weight:700;letter-spacing:1.5px;text-transform:uppercase}
.btn-light{background:var(--white);color:var(--purple)}
.btn-purple{background:var(--purple);color:var(--white)}

/* hero */
.hero{left:17px;top:15px;width:1166px;height:752px}
.hero .photo{background:radial-gradient(ellipse at 55% 45%,#8a6a52 0%,#6a5140 35%,#3f342d 75%,#2a2521 100%)}
.brand-mark{position:absolute;left:34px;top:40px;display:flex;align-items:center;gap:8px;color:var(--white);font-family:'Montserrat',sans-serif;font-weight:800;font-size:13px;line-height:15px;width:170px}
.brand-mark .sq{width:12px;height:12px;background:var(--purple-soft);flex:none}
.menu-btn{position:absolute;left:1005px;top:48px;width:50px;height:50px;border-radius:50%;background:var(--white);display:flex;align-items:center;justify-content:center}
.hero-title{position:absolute;left:100px;top:88px;width:1000px;text-align:center;font-size:100px;line-height:120px}
.hero-copy{left:815px;top:495px;width:250px}
.hero .btn{left:815px;top:640px;width:163px;height:41px}

/* build */
.build{left:17px;top:783px;width:1166px;height:750px}
.build .photo{background:linear-gradient(120deg,#d8cfc4 0%,#b38a5a 30%,#8c6440 50%,#cbbfb0 80%,#e6e0d8 100%)}
.build-title{position:absolute;left:398px;top:80px;font-size:86px;line-height:100px}
.build-copy{left:640px;top:400px;width:430px}
.build-copy p+p{margin-top:24px}
.build .btn{left:441px;top:623px;width:163px;height:40px}

/* renovations banner */
.reno{left:17px;top:1548px;width:1166px;height:494px}
.reno .photo{background:linear-gradient(180deg,#6d5a4a 0%,#a8916f 45%,#7a5a3c 75%,#5a3c25 100%)}
.reno-title{position:absolute;left:108px;top:298px;font-size:56px;line-height:66px}

/* gallery */
.shot{position:absolute}
.shot-a{left:17px;top:2057px;width:566px;height:703px;background:linear-gradient(90deg,#8a5a33 0%,#c89a68 40%,#e8dccb 60%,#9b6a3f 100%)}
.shot-b{left:602px;top:2057px;width:572px;height:342px;background:linear-gradient(135deg,#e9e6e2 0%,#b9a792 50%,#6e5138 100%)}
.shot-c{left:602px;top:2418px;width:572px;height:342px;background:linear-gradient(135deg,#4a433d 0%,#9a7a58 45%,#e2ddd5 100%)}

/* services */
.services{left:17px;top:2775px;width:1166px;height:752px}
.services .photo{background:linear-gradient(180deg,#6e7377 0%,#7f8488 50%,#6a6f73 100%)}
.person{position:absolute;left:455px;top:40px;width:260px;height:712px;background:linear-gradient(180deg,#5a4236 0%,#c9a28a 25%,#f1ece8 45%,#a63a3a 65%,#d99a2b 100%);border-radius:110px 110px 0 0}
.services-title{position:absolute;left:0;top:40px;width:1166px;text-align:center;font-size:82px;line-height:98px}
.service{position:absolute;color:var(--white)}
.service h3{font-family:'Montserrat',sans-serif;font-weight:800;font-size:32px;line-height:40px}
.service p{margin-top:28px;font-size:14px;line-height:28px;font-weight:500}
.service-left{left:120px;top:372px;width:260px;text-align:right}
.service-right{left:793px;top:372px;width:270px}
.services .btn{left:501px;top:634px;width:165px;height:37px}

/* testimonials */
.reviews{left:0;top:3536px;width:1200px;height:420px;background:var(--purple-mist)}
.card{position:absolute;top:14px;width:280px;height:392px;background:var(--white);box-shadow:0 4px 16px rgba(0,0,0,.06);padding:26px 30px}
.card-head{display:flex;align-items:center;gap:14px}
.avatar{width:40px;height:40px;border-radius:50%;flex:none}
.card-name{font-family:'Montserrat',sans-serif;font-weight:800;font-size:15px;line-height:18px}
.card-role{font-size:11px;color:#999}
.card p{margin-top:24px;font-size:11.5px;line-height:20px;color:var(--grey-text)}
.stars{position:absolute;left:30px;bottom:26px;color:var(--gold);font-size:15px;letter-spacing:8px}
.nav-arrow{position:absolute;top:185px;width:48px;height:48px;border-radius:50%;background:var(--purple);display:flex;align-items:center;justify-content:center}

/* contact */
.contact{left:0;top:3964px;width:1200px;height:442px;background:var(--ink)}
.contact h2{position:absolute;left:125px;top:120px;font-family:'Montserrat',sans-serif;font-weight:800;font-size:48px;color:var(--white)}
.contact-line{position:absolute;left:125px;display:flex;align-items:center;gap:22px;color:var(--white);font-size:14px}
.contact-line .ico{width:34px;height:34px;border-radius:50%;background:var(--purple);display:flex;align-items:center;justify-content:center}
.contact-intro{position:absolute;left:613px;top:72px;width:300px;color:var(--white);font-size:11px;line-height:22px}
.field{position:absolute;left:613px;width:384px;border:1px solid #8c8c8c;color:var(--white);font-size:10px;padding:12px 14px 0}

/* footer */
.footer{left:0;top:4406px;width:1200px;height:344px;background:var(--white)}
.footer-brand{position:absolute;left:125px;top:142px;display:flex;align-items:center;gap:12px;font-family:'Montserrat',sans-serif;font-weight:800;font-size:22px;line-height:26px;color:var(--purple);width:260px}
.footer-brand .sq{width:22px;height:22px;background:var(--purple);flex:none}
.social{position:absolute;top:128px;width:38px;height:38px;border-radius:50%;background:var(--ink)}
.footer-nav{position:absolute;left:598px;top:200px;display:flex;gap:36px;font-size:13px;color:var(--ink)}
.bottom-bar{left:0;top:4750px;width:1200px;height:68px;background:var(--ink-deep);color:var(--white);font-size:11px;display:flex;align-items:center;justify-content:center}
</style>
</head>
<body>

<section class="block hero">
  <div class="photo" role="img" aria-label="Carpenter in a plaid shirt and apron standing with arms crossed in a workshop"></div>
  <svg class="deco" viewBox="0 0 1166 752" preserveAspectRatio="none" aria-hidden="true">
    <polygon points="230,0 300,0 30,752 0,752 0,640" fill="#2b2b2b" opacity=".75"/>
    <polygon points="130,0 235,0 40,752 0,752 0,560" fill="#6B429C" opacity=".9"/>
  </svg>
  <div class="brand-mark"><span class="sq"></span>Kestrel Joinery Works Limited</div>
  <div class="menu-btn"><svg width="20" height="16" viewBox="0 0 20 16"><rect y="1" width="20" height="2.5" rx="1" fill="#6B429C"/><rect y="7" width="20" height="2.5" rx="1" fill="#6B429C"/><rect y="13" width="20" height="2.5" rx="1" fill="#6B429C"/></svg></div>
  <h1 class="display hero-title">Quality<br><span class="outline">Craftsmanship</span><br>At Your <span class="outline">Service</span></h1>
  <p class="copy hero-copy">Lorem Ipsum is simply dummy text of the printing and typesetting industry. Lorem Ipsum has been the industry's standard dummy text ever since the 1500s,</p>
  <div class="btn btn-light">Contact Us</div>
</section>

<section class="block build">
  <div class="photo" role="img" aria-label="Carpenter in a brown shirt marking timber with a pencil"></div>
  <svg class="deco" viewBox="0 0 1166 750" preserveAspectRatio="none" aria-hidden="true">
    <polygon points="1166,0 1166,750 560,750" fill="#3d3d3f"/>
  </svg>
  <h2 class="display build-title">Build Your<br><span class="outline">Dr</span>eam With<br><span class="outline">Ca</span>rpenter</h2>
  <div class="copy build-copy">
    <p>Lorem Ipsum is simply dummy text of the printing and typesetting industry. Lorem Ipsum has been the industry's standard dummy text ever since the 1500s, when an unknown printer took a galley of type and scrambled it to make a type specimen book.</p>
    <p>It has survived not only five centuries, but also the leap into electronic typesetting, remaining essentially unchanged. It was popularised in the 1960s with the release of Printwell sheets containing Lorem Ipsum passages, and more recently with desktop publishing software like LayoutPress including versions of Lorem Ipsum.</p>
  </div>
  <div class="btn btn-light">Read More</div>
</section>

<section class="block reno">
  <div class="photo" role="img" aria-label="Renovated living room with timber floors and tall glass doors"></div>
  <svg class="deco" viewBox="0 0 1166 494" preserveAspectRatio="none" aria-hidden="true">
    <polygon points="150,0 250,0 60,494 0,494 0,330" fill="#6B429C" opacity=".85"/>
    <polygon points="290,0 420,0 200,494 90,494" fill="#6B429C" opacity=".55"/>
  </svg>
  <h2 class="display reno-title">Some Renovations<br>From Our Work</h2>
</section>

<div class="shot shot-a" role="img" aria-label="Hallway lined with vertical timber battens and pendant lights"></div>
<div class="shot shot-b" role="img" aria-label="Entry with timber staircase and wooden front door"></div>
<div class="shot shot-c" role="img" aria-label="Living space with stone wall, timber bench and glass doors"></div>

<section class="block services">
  <div class="photo" role="img" aria-label="Concrete wall backdrop"></div>
  <svg class="deco" viewBox="0 0 1166 752" preserveAspectRatio="none" aria-hidden="true">
    <polygon points="0,0 190,0 0,330" fill="#3d3d3f"/>
    <polygon points="1166,0 1166,752 740,752" fill="#6B429C" opacity=".9"/>
  </svg>
  <div class="person" role="img" aria-label="Smiling tradeswoman in a plaid shirt wearing a tool belt"></div>
  <h2 class="display services-title">Some Services<br>Which We Provide</h2>
  <div class="service service-left"><h3>Exterior<br>Renovation</h3><p>Lorem Ipsum is simply dummy text of the printing and typesetting industry. Lorem Ipsum has been the industry's standard dummy text ever since the 1500s,</p></div>
  <div class="service service-right"><h3>Interior<br>Renovation</h3><p>Lorem Ipsum is simply dummy text of the printing and typesetting industry. Lorem Ipsum has been the industry's standard dummy text ever since the 1500s,</p></div>
  <div class="btn btn-purple">View All</div>
</section>

<section class="block reviews">
  <article class="card" style="left:17px"><div class="card-head"><div class="avatar" role="img" aria-label="Reviewer portrait" style="background:#7a6a5e"></div><div><div class="card-name">Mara Whitlow</div><div class="card-role">Business Name</div></div></div><p>Lorem Ipsum is simply dummy text of the printing and typesetting industry. Lorem Ipsum has been the industry's standard dummy text ever since the 1500s, when an unknown printer took a galley of type and scrambled it to make a type specimen book. It has survived not only five centuries, but also the leap into electronic typesetting, remaining essentially unchanged.</p><div class="stars">★★★★★</div></article>
  <article class="card" style="left:312px"><div class="card-head"><div class="avatar" role="img" aria-label="Reviewer portrait" style="background:#c9a58e"></div><div><div class="card-name">Mara Whitlow</div><div class="card-role">Business Name</div></div></div><p>Lorem Ipsum is simply dummy text of the printing and typesetting industry. Lorem Ipsum has been the industry's standard dummy text ever since the 1500s, when an unknown printer took a galley of type and scrambled it to make a type specimen book. It has survived not only five centuries, but also the leap into electronic typesetting, remaining essentially unchanged.</p><div class="stars">★★★★★</div></article>
  <article class="card" style="left:608px"><div class="card-head"><div class="avatar" role="img" aria-label="Reviewer portrait" style="background:#8a7a70"></div><div><div class="card-name">Mara Whitlow</div><div class="card-role">Business Name</div></div></div><p>Lorem Ipsum is simply dummy text of the printing and typesetting industry. Lorem Ipsum has been the industry's standard dummy text ever since the 1500s, when an unknown printer took a galley of type and scrambled it to make a type specimen book. It has survived not only five centuries, but also the leap into electronic typesetting, remaining essentially unchanged.</p><div class="stars">★★★★★</div></article>
  <article class="card" style="left:903px"><div class="card-head"><div class="avatar" role="img" aria-label="Reviewer portrait" style="background:#d9a04a"></div><div><div class="card-name">Mara Whitlow</div><div class="card-role">Business Name</div></div></div><p>Lorem Ipsum is simply dummy text of the printing and typesetting industry. Lorem Ipsum has been the industry's standard dummy text ever since the 1500s, when an unknown printer took a galley of type and scrambled it to make a type specimen book. It has survived not only five centuries, but also the leap into electronic typesetting, remaining essentially unchanged.</p><div class="stars">★★★★★</div></article>
  <div class="nav-arrow" style="left:59px"><svg width="14" height="14" viewBox="0 0 14 14"><path d="M9 2 4 7l5 5" fill="none" stroke="#fff" stroke-width="2.5"/></svg></div>
  <div class="nav-arrow" style="left:1093px"><svg width="14" height="14" viewBox="0 0 14 14"><path d="M5 2l5 5-5 5" fill="none" stroke="#fff" stroke-width="2.5"/></svg></div>
</section>

<section class="block contact">
  <svg class="deco" viewBox="0 0 1200 442" preserveAspectRatio="none" aria-hidden="true">
    <polygon points="1200,20 1200,110 1110,300 1080,300" fill="#6B429C"/>
  </svg>
  <p class="contact-intro">Lorem Ipsum is simply dummy text of the printing and typesetting industry.</p>
  <h2>Contact Us</h2>
  <div class="contact-line" style="top:206px"><span class="ico"><svg width="14" height="14" viewBox="0 0 24 24"><path d="M6.6 10.8a15 15 0 0 0 6.6 6.6l2.2-2.2a1 1 0 0 1 1-.25 11.4 11.4 0 0 0 3.6.6 1 1 0 0 1 1 1V20a1 1 0 0 1-1 1A17 17 0 0 1 3 4a1 1 0 0 1 1-1h3.5a1 1 0 0 1 1 1c0 1.25.2 2.45.6 3.6a1 1 0 0 1-.25 1z" fill="#fff"/></svg></span>+64 210 448 27</div>
  <div class="contact-line" style="top:269px"><span class="ico"><svg width="14" height="12" viewBox="0 0 24 18"><rect x="1" y="1" width="22" height="16" rx="2" fill="#fff"/><path d="M2 2l10 8 10-8" fill="none" stroke="#6B429C" stroke-width="2"/></svg></span>hello@kestreljoinery.example</div>
  <div class="field" style="top:137px;height:39px">Name</div>
  <div class="field" style="top:191px;height:39px">Email</div>
  <div class="field" style="top:245px;height:107px">Message
    <svg style="position:absolute;right:14px;bottom:12px" width="14" height="14" viewBox="0 0 14 14"><path d="M1 13 13 7 1 1l2 6z" fill="#6B429C"/></svg>
  </div>
</section>

<footer class="block footer">
  <div class="footer-brand"><span class="sq"></span>Kestrel Joinery Works Limited</div>
  <span class="social" style="left:935px" aria-label="Social profile"></span>
  <span class="social" style="left:985px" aria-label="Social profile"></span>
  <span class="social" style="left:1038px" aria-label="Social profile"></span>
  <nav class="footer-nav"><span>Home</span><span>About Us</span><span>Renovation</span><span>Testimonials</span><span>Contact Us</span></nav>
</footer>
<div class="block bottom-bar">© 2023 Kestrel Joinery Works. All Rights Reserved.</div>

</body>
</html>
```